Calloway Dental Care

I need a nice business card design that is double sided. This is for a dental surgery. I have already had a logo designed and just need the business card put together.

It needs to be in a format such that I can make new business cards if new dentists begin working for me. Hence I need to be able to change the text in order to have new names written on new cards.

The front will have the following text:

Dr Tariq Mansour
B. Med. Sci. QBTU B.Dent. Brel. Uni

The logo will appear somewhere on the front. This is attached.

In addition will be the following writing that also needs to appear on the front of the card, perhaps at the bottom on the left side will be:

Shop 4, 212-240 Parlow Street, North Sydney, NSW, 2060

and at the bottom on the right side will be:
(02) 5550 1736
e: info@callowaydentalcare.com.au
www.callowaydentalcare.com.au

On the back of the card will be a section for a map to be drawn (I have uploaded a picture) and also a section written as follows:

"Your next appointment is: (a line needs to be here to write date and time)"

Also I need two lines for two appointments to be written.

Thanks for your efforts!

```html
<!DOCTYPE html>
<html lang="en">
<head>
<meta charset="utf-8">
<title>Calloway Dental Care – Business Card</title>
<link rel="stylesheet" href="https://fonts.googleapis.com/css2?family=Source+Sans+3:wght@400;600&display=swap">
<style>
  :root {
    --backdrop: #e9e4dc;
    --card: #ffffff;
    --band-blue: #2a66cc;
    --band-cyan: #5ef0f0;
    --text-blue: #2a6bd0;
    --text-cyan: #55dff0;
    --faint: rgba(120, 200, 225, 0.28);
    --map-tone: #eef0f2;
    --map-line: #222222;
  }
  * { box-sizing: border-box; margin: 0; padding: 0; }
  html, body { width: 1200px; height: 686px; overflow: hidden; }
  body {
    background: var(--backdrop);
    font-family: "Source Sans 3", "Myriad Pro", sans-serif;
    color: var(--text-blue);
    position: relative;
  }
  .card {
    position: absolute;
    width: 432px;
    height: 247px;
    background: var(--card);
    overflow: hidden;
    box-shadow: 0 2px 6px rgba(0,0,0,0.12);
  }
  .card--front { left: 228px; top: 104px; }
  .card--back  { left: 552px; top: 362px; }

  .band-cyan { position: absolute; left: 0; width: 100%; height: 7px; background: var(--band-cyan); }
  .band-blue { position: absolute; left: 0; width: 100%; height: 41px; background: var(--band-blue); }

  .brand {
    position: absolute; left: 10px; top: 22px;
    display: flex; align-items: center; gap: 5px;
    font-size: 11px; font-weight: 600; letter-spacing: 0.5px;
    color: var(--text-blue); text-transform: uppercase;
  }
  .brand__dot { width: 10px; height: 10px; border-radius: 50%; background: var(--text-cyan); }

  .brand-faint {
    position: absolute;
    font-size: 26px; font-weight: 600; letter-spacing: 2px;
    color: var(--faint); text-transform: uppercase;
  }

  .dentist {
    position: absolute; right: 12px; top: 12px; text-align: right;
  }
  .dentist__name { font-size: 23px; font-weight: 400; line-height: 1.1; padding-right: 9px; }
  .dentist__quals { font-size: 12px; color: var(--text-cyan); margin-top: 4px; }

  .address {
    position: absolute; left: 4px; top: 161px;
    font-size: 11.5px; line-height: 15px;
  }
  .contact {
    position: absolute; left: 260px; top: 148px;
    font-size: 11.5px; line-height: 14.5px;
  }

  .next-appt {
    position: absolute; left: 0; right: 0; top: 70px;
    text-align: center; font-size: 13px;
  }
  .blank { display: inline-block; border-bottom: 1px solid var(--text-blue); vertical-align: baseline; height: 1px; }
  .appt-line { position: absolute; left: 9px; font-size: 13px; }
  .appt-line--1 { top: 145px; }
  .appt-line--2 { top: 184px; }

  .map {
    position: absolute; left: 275px; top: 144px;
    width: 140px; height: 84px;
    border: 1px solid var(--map-line);
    background: var(--map-tone);
  }
</style>
</head>
<body>

  <section class="card card--front" aria-label="Business card front">
    <div class="brand"><span class="brand__dot"></span>Calloway</div>
    <div class="brand-faint" style="left:180px; top:140px;">Calloway</div>

    <div class="dentist">
      <h1 class="dentist__name">Dr Tariq Mansour</h1>
      <p class="dentist__quals">B.Med.Sci.QBTU B.Dent.Brel.Uni</p>
    </div>

    <address class="address" style="font-style:normal;">
      Shop 4, 212-240 Parlow Street,<br>
      North Sydney,NWS,2060.
    </address>

    <div class="contact">
      (02) 5550 1736<br>
      e:info@callowaydentalcare.com.au<br>
      www.callowaydentalcare.com.au
    </div>

    <div class="band-cyan" style="top:193px;"></div>
    <div class="band-blue" style="top:200px;"></div>
    <div class="band-cyan" style="top:240px;"></div>
  </section>

  <section class="card card--back" aria-label="Business card back">
    <div class="band-cyan" style="top:0;"></div>
    <div class="band-blue" style="top:7px;"></div>
    <div class="band-cyan" style="top:48px; height:6px;"></div>

    <div class="brand-faint" style="left:150px; top:158px;">Calloway</div>

    <p class="next-appt">Your next appointment is:&nbsp; Date<span class="blank" style="width:62px;"></span> Time <span class="blank" style="width:68px;"></span></p>

    <p class="appt-line appt-line--1">Appointment: 1</p>
    <p class="appt-line appt-line--2">Appointment: 2</p>

    <div class="map" role="img" aria-label="Street map showing the location of Calloway Dental Care"></div>
  </section>

</body>
</html>
```